Business Card Design Project: Classically Trained Singer and Voice Teacher

I am a classically trained singer that performs in Opera and Musical Theater and also teaches private voice lessons in those fields. I am looking for a business card that I can give to casting directors and colleagues, as well as to people who are interested in taking voice lessons from me.

This is sort of like an actors business card so I want my headshot and name to be the main focus.

I was kind of thinking of having the business card be horizontal with my headshot photo on the front taking up roughly half and my information on the same side, and perhaps my name again on the back or some form of my initials. But I am totally open to other options for layout.I would prefer to have a double sided business card, but once again, its not essential.

I am looking for it to look and feel elegant artistic and professional, without looking feminine.

Because of the colors of my headshot I would imagine that it would be predominantly brown and white, but I am totally open to other approaches.feel totally free to crop my headshot so that it fits better into your overall design and layout.

It is highly likely that I will ask the winner of the design to create a flyer for marketing my voice lessons with a similar look.

If you have any questions or clarifications, please feel free to ask.

Target Market(s)

Opera and Musical theater casting directors, colleagues; potential voice lesson students

Industry/Entity Type

Marketing

Requirements
Must have
• These must feature prominently:
- (My Headshot (attached))
- Marlow Keaton (my name)

These dont need to be as prominent:
- Baritone
- Private Voice Teacher
- Opera and Musical Theater

Contact Info:
Phone: (530) 555-0147
Email: markeat@inboxly.example

Nice to have
• Double sided

```html
<!DOCTYPE html>
<html lang="en">
<head>
<meta charset="utf-8">
<title>Marlow Keaton — Business Card</title>
<link rel="stylesheet" href="https://fonts.googleapis.com/css2?family=Anton&family=Quicksand:wght@400;500&display=swap">
<style>
  :root {
    --page-bg: #e9e4d6;
    --card-black: #000000;
    --coral: #ff6f6a;
    --name-red: #8a0f14;
    --ink-white: #ffffff;
    --photo-deep: #4a3a6e;
    --photo-warm: #9a5a3c;
    --photo-light: #f4ecd0;
  }
  * { box-sizing: border-box; margin: 0; padding: 0; }
  html, body {
    width: 1200px; height: 1200px; overflow: hidden;
    background: var(--page-bg);
  }
  .canvas { position: relative; width: 1200px; height: 1200px; }

  .card {
    position: absolute; top: 206px;
    width: 521px; height: 828px;
    background: var(--card-black);
    overflow: hidden;
  }
  .card--front { left: 53px; }
  .card--back { left: 626px; }

  .headshot {
    position: absolute; left: 0; top: 28px;
    width: 521px; height: 771px;
    background:
      radial-gradient(ellipse 45% 35% at 55% 40%, var(--photo-light) 0%, rgba(244,236,208,0) 70%),
      linear-gradient(180deg, #7c6f9c 0%, var(--photo-deep) 35%, var(--photo-warm) 70%, #5a3248 100%);
  }

  .name-plate {
    position: absolute; left: 88px; top: 688px;
    width: 358px; height: 140px;
    background: var(--coral);
    display: flex; align-items: center; justify-content: center;
  }
  .name-plate__text {
    font-family: "Anton", "Oswald", sans-serif;
    font-size: 58px; letter-spacing: -1px;
    color: var(--name-red);
    text-transform: uppercase;
    line-height: 1;
  }

  .details {
    position: absolute; left: 0; width: 100%;
    text-align: center;
    font-family: "Quicksand", sans-serif;
    color: var(--ink-white);
  }
  .details--roles { top: 210px; }
  .details__voice { font-size: 37px; line-height: 50px; font-weight: 500; }
  .details__role { font-size: 37px; line-height: 50px; font-weight: 500; }
  .details__genre { font-size: 29px; line-height: 38px; font-weight: 500; }

  .details--contact { top: 448px; color: var(--coral); }
  .details__phone { font-size: 37px; line-height: 52px; }
  .details__email { font-size: 33px; line-height: 48px; }
</style>
</head>
<body>
  <main class="canvas">
    <section class="card card--front">
      <div class="headshot" role="img" aria-label="Headshot of the singer in a brown jacket and striped shirt"></div>
      <div class="name-plate">
        <span class="name-plate__text">Marlow Keaton</span>
      </div>
    </section>

    <section class="card card--back">
      <div class="details details--roles">
        <p class="details__voice">Baritone</p>
        <p class="details__role">Private Voice Teacher</p>
        <p class="details__genre">Opera and Musical Theater</p>
      </div>
      <div class="details details--contact">
        <p class="details__phone">(530) 555-0147</p>
        <p class="details__email">markeat@inboxly.example</p>
      </div>
    </section>
  </main>
</body>
</html>
```